Family Owned Construction Company Needs Modern Business Cards

We need a new design for our business cards. We are a family owned construction company, Brantwell Construction, based in Mendon, Vermont and would like to add in our new logo and find a more modern look. We also want to use our old to make sure people know who we are. We do site development, highway, environmental, demolition, utility and aggregate.

Contact Information for Business Card

We want to have the office address, 418 Quarry Ridge Road, Harlow Falls, KR 05788 and our phone (802) 555-0137 and fax (802) 555-0164 on there as well. Our website is www.brantwellinc.example. There should be a place for the person's name, title, cell number, and email address on the card. Words that we would like to be associated with our company are honesty, predictable, reliable, integrity, dedicated, built right quality, consistent, whatever it takes, and innovation. Safety is also very important to us.

Font styles to use
Serif
Sans Serif
Other font styles liked:
• Square 721 Extented

Colors
0255a3
ffffff

Requirements
Must have
• Office address, phone number and fax number. New logo with excavator
Nice to have
• That we do site development, highway, environmental, demolition, utility, and aggregate. Both logos

```html
<!DOCTYPE html>
<html lang="en">
<head>
<meta charset="utf-8">
<title>Brantwell Construction – Business Cards</title>
<link href="https://fonts.googleapis.com/css2?family=Montserrat:wght@600;700&family=Work+Sans:wght@400;600;800&display=swap" rel="stylesheet">
<style>
  :root {
    --navy: #1b3462;
    --navy-light: #25457a;
    --white: #ffffff;
    --backdrop: #e6e8ec;
  }
  * { box-sizing: border-box; margin: 0; padding: 0; }
  html, body {
    width: 1200px; height: 1000px; overflow: hidden;
    background: var(--backdrop);
    font-family: "Work Sans", Arial, sans-serif;
  }
  .card {
    position: absolute; left: 250px;
    width: 700px; height: 400px;
    overflow: hidden;
    box-shadow: 0 6px 18px rgba(0,0,0,.18);
  }
  .card--front {
    top: 50px;
    background: linear-gradient(160deg, var(--navy) 0%, var(--navy-light) 100%);
    color: var(--white);
    text-align: center;
  }
  .wordmark {
    font-family: "Work Sans", Arial, sans-serif;
    font-weight: 800;
    line-height: 1;
    letter-spacing: 1px;
  }
  .wordmark__name { display: block; font-size: 52px; }
  .wordmark__sub { display: block; font-size: 20px; letter-spacing: 4px; margin-top: 6px; }
  .card--front .wordmark { position: absolute; top: 120px; left: 0; right: 0; color: var(--white); }
  .services {
    position: absolute; top: 270px; left: 0; right: 0;
    font-size: 17px; line-height: 1.35; letter-spacing: .5px;
  }
  .card--back { top: 510px; background: var(--white); }
  .card--back .wordmark {
    position: absolute; top: 62px; left: 0; right: 0; text-align: center;
    color: var(--navy);
  }
  .card__band {
    position: absolute; left: 0; right: 0; bottom: 0; height: 175px;
    background: var(--navy); color: var(--white);
  }
  .person { position: absolute; left: 34px; top: 20px; width: 268px; }
  .person__name { font-family: "Montserrat", Arial, sans-serif; font-weight: 700; font-size: 27px; line-height: 1.2; }
  .person__title { font-family: "Montserrat", Arial, sans-serif; font-weight: 600; font-size: 17px; text-align: right; }
  .person__address { font-size: 16px; letter-spacing: 1px; line-height: 1.4; margin-top: 8px; }
  .divider { position: absolute; left: 318px; top: 30px; width: 2px; height: 115px; background: var(--white); }
  .contacts { position: absolute; left: 345px; top: 30px; list-style: none; }
  .contacts li { display: flex; align-items: center; font-size: 17px; letter-spacing: .8px; height: 29px; }
  .contacts svg { width: 16px; height: 16px; margin-right: 18px; fill: var(--white); flex: none; }
</style>
</head>
<body>
  <section class="card card--front">
    <div class="wordmark">
      <span class="wordmark__name">BRANTWELL</span>
      <span class="wordmark__sub">CONSTRUCTION INC.</span>
    </div>
    <p class="services">site development | highway<br>environmental | demolition | utility | aggregate</p>
  </section>

  <section class="card card--back">
    <div class="wordmark">
      <span class="wordmark__name">BRANTWELL</span>
      <span class="wordmark__sub">CONSTRUCTION INC.</span>
    </div>
    <div class="card__band">
      <div class="person">
        <p class="person__name">Dorian Vale</p>
        <p class="person__title">Founder</p>
        <p class="person__address">418 Quarry Ridge Road<br>Harlow Falls, KR 05788</p>
      </div>
      <div class="divider"></div>
      <ul class="contacts">
        <li><svg viewBox="0 0 16 16" aria-hidden="true"><path d="M2 5c0-2 2-3 6-3s6 1 6 3v1h-3V5H5v1H2zM4 7h8l2 7H2z"/></svg>(802) 555-0137</li>
        <li><svg viewBox="0 0 16 16" aria-hidden="true"><path d="M4 1h8v5H4zM1 6h14v9H1zM4 9h8v1H4zM4 11h8v1H4z"/></svg>(802) 555-0164</li>
        <li><svg viewBox="0 0 16 16" aria-hidden="true"><path d="M1 3h14v10H1zM2 4l6 5 6-5v-.2H2z" fill-rule="evenodd"/></svg>info@dorianvale.example</li>
        <li><svg viewBox="0 0 16 16" aria-hidden="true"><circle cx="8" cy="8" r="7"/><path d="M1 8h14M8 1c3 3 3 11 0 14M8 1c-3 3-3 11 0 14" stroke="#1b3462" stroke-width="1" fill="none"/></svg>www.brantwellinc.example</li>
      </ul>
    </div>
  </section>
</body>
</html>
```